2009 Thank You

A colorful post card that is 8.5 x 5.5.  The purpose is to say thank you to our customers and to wish them a prosperous new year.  We a printing company and will print 4-color process on both sides of the post card

• I have included our logo to be incorporated where appropriate 

• The theme might incorporate something that recognizes "these are turbulent times"  or "success from adversity"

```html
<!DOCTYPE html>
<html lang="en">
<head>
<meta charset="utf-8">
<title>2009 Thank You Postcard – Inkwell Press</title>
<link rel="stylesheet" href="https://fonts.googleapis.com/css2?family=Arimo:wght@400&family=Roboto+Condensed:wght@400&display=swap">
<style>
  :root {
    --paper: #ffffff;
    --ink: #1a1a1a;
    --trim: #9a9a9a;
    --panel: rgba(255, 255, 255, 0.86);
    --ochre: #c99a3a;
    --gold: #f2c230;
    --magenta: #d6317a;
    --crimson: #c8202e;
    --green: #2fa84a;
    --teal: #1a8fb0;
    --violet: #5a2d8c;
    --orange: #f07a1e;
  }
  * { box-sizing: border-box; margin: 0; padding: 0; }
  html, body {
    width: 1200px; height: 830px; overflow: hidden;
    background: var(--paper);
  }
  .sheet { position: relative; width: 1200px; height: 830px; }
  .crop-marks { position: absolute; inset: 0; }
  .postcard {
    position: absolute; left: 73px; top: 73px; width: 1055px; height: 683px;
    overflow: hidden;
  }
  .postcard__art {
    position: absolute; inset: 0;
    background:
      radial-gradient(ellipse 30% 40% at 95% 25%, var(--teal) 0%, transparent 70%),
      radial-gradient(ellipse 28% 35% at 78% 12%, var(--magenta) 0%, transparent 70%),
      radial-gradient(ellipse 30% 35% at 60% 8%, var(--crimson) 0%, transparent 70%),
      radial-gradient(ellipse 30% 40% at 90% 60%, var(--violet) 0%, transparent 70%),
      radial-gradient(ellipse 30% 35% at 75% 45%, var(--green) 0%, transparent 70%),
      radial-gradient(ellipse 35% 30% at 85% 95%, var(--orange) 0%, transparent 70%),
      radial-gradient(ellipse 40% 30% at 55% 95%, var(--gold) 0%, transparent 70%),
      radial-gradient(ellipse 45% 60% at 15% 45%, #f4d98a 0%, transparent 75%),
      linear-gradient(100deg, var(--ochre) 0%, #e6c472 35%, #f0b04a 60%, #b23a6a 100%);
  }
  .message-panel {
    position: absolute; left: 126px; top: 119px; width: 804px; height: 436px;
    background: var(--panel);
    box-shadow: 0 2px 10px rgba(0, 0, 0, 0.35);
  }
  .message {
    position: absolute; left: 34px; top: 46px; width: 479px;
    font-family: "Arimo", Arial, sans-serif;
    font-size: 17.6px; line-height: 27.6px; color: var(--ink);
    text-align: justify;
  }
  .message p + p { margin-top: 27.6px; }
  .message .signoff { text-align: left; }
  .brand {
    position: absolute; left: 524px; top: 44px;
    font-family: "Arimo", Arial, sans-serif;
    font-weight: 400; font-size: 38px; line-height: 1; color: var(--ink);
    white-space: nowrap;
  }
  .contact {
    position: absolute; left: 524px; top: 242px;
    font-family: "Roboto Condensed", "Arial Narrow", sans-serif;
    font-style: normal;
    font-size: 14.5px; letter-spacing: 2.2px; line-height: 29.4px; color: var(--ink);
  }
  .contact .web { margin-top: 24px; }
</style>
</head>
<body>
<div class="sheet">
  <svg class="crop-marks" width="1200" height="830" viewBox="0 0 1200 830" aria-hidden="true">
    <g stroke="var(--trim)" stroke-width="1">
      <line x1="73" y1="0" x2="73" y2="52"/><line x1="0" y1="73" x2="52" y2="73"/>
      <line x1="1128" y1="0" x2="1128" y2="52"/><line x1="1148" y1="73" x2="1200" y2="73"/>
      <line x1="73" y1="778" x2="73" y2="830"/><line x1="0" y1="756" x2="52" y2="756"/>
      <line x1="1128" y1="778" x2="1128" y2="830"/><line x1="1148" y1="756" x2="1200" y2="756"/>
    </g>
  </svg>

  <section class="postcard">
    <div class="postcard__art" role="img" aria-label="Colourful paint splatter artwork over a warm gold background with a repeating faint 2009 pattern"></div>

    <div class="message-panel">
      <div class="message">
        <p>In these turbulent times it’s easy to forget that good things that are happening all around. With this in mind, we just wanted to say thank you for your business in 2008.</p>
        <p>We hope you will enjoy a prosperous year in 2009. If there is anything we can do to help your company succeed, please give us a call. We are happy to provide printing services of all types including brochures, direct mail, multi-media campaigns to drive internet traffic, training materials and fulfillment services.</p>
        <p class="signoff">Give us a call!</p>
      </div>

      <div class="brand">Inkwell Press</div>

      <address class="contact">
        <div>2150 Harlow Ave.</div>
        <div>Unit # 7, Denver, Co 80216</div>
        <div>Phone: (303) 555-0142</div>
        <div class="web">Web.: www.inkwellpress.com</div>
      </address>
    </div>
  </section>
</div>
</body>
</html>
```